Design for Card Attached to Clothes

We sell rhythmic gymnastics apparel and are looking for someone create a card that will be attached to the products. You can see an example of the exact type of apparel in the files, as well as the current card that is attached to it. The design should have space on the top back for the sticker that has UPC and SKU information, as shown in the image attached.
- We would like the front to have our logo
- We would like the image of the girls added on the back
- Would be cool to see the gradient change to the white space on the back where the sticker will go but not required.
-The final card size is 10cm by 6cm, Their should be 2mm loss accounted for cutting the cards within the design. (meaning the design needs to be bigger than 10cm by 6cm to account for printing and cut)
- And the hole size that is at the top center is 3mm in diameter
- Name should be under logo
Access all logo files here https://files.plomvarek.net/share/folders/7Kq2TzWm9RbXa4LpYc8NdVe3Hs5JfGu1?view=open
- Front will have logo
- Back will have image of girls and some creative design that you will create.
Females
Rhythmic Gymnastics

```html
<!DOCTYPE html>
<html lang="en">
<head>
<meta charset="utf-8">
<title>Velora hang tags</title>
<link rel="stylesheet" href="https://fonts.googleapis.com/css2?family=Quicksand:wght@500&family=Mrs+Saint+Delafield&display=swap">
<style>
  :root {
    --backdrop: #cbcbcb;
    --card: #ffffff;
    --magenta: #e5127d;
    --magenta-deep: #d0177f;
    --magenta-soft: #e98fc0;
    --ink: #1a1a1a;
    --hole-dark: #3a3a40;
    --tone-skin: #d9a98a;
    --tone-black: #222226;
  }
  html, body {
    margin: 0;
    width: 1200px;
    height: 1000px;
    overflow: hidden;
    background: var(--backdrop);
  }
  .canvas {
    position: relative;
    width: 1200px;
    height: 1000px;
  }
  .tag {
    position: absolute;
    top: 225px;
    width: 354px;
    height: 589px;
    background: var(--card);
    box-shadow: 0 2px 8px rgba(0,0,0,0.35);
    overflow: hidden;
  }
  .tag--front { left: 157px; }
  .tag--back { left: 677px; }

  .hole {
    position: absolute;
    top: 49px;
    left: 170px;
    width: 14px;
    height: 14px;
    border-radius: 50%;
  }
  .tag--front .hole { background: var(--card); }
  .tag--back .hole { background: var(--hole-dark); }

  .front-band {
    position: absolute;
    inset: 0 0 auto 0;
    height: 162px;
    background: linear-gradient(to bottom, var(--magenta-deep) 0%, var(--magenta-soft) 55%, var(--card) 100%);
  }

  .brand {
    position: absolute;
    left: 0;
    right: 0;
    text-align: center;
    font-family: "Quicksand", sans-serif;
    font-weight: 500;
    color: var(--magenta);
    margin: 0;
    line-height: 1;
  }
  .brand-dot {
    position: absolute;
    border-radius: 50%;
    background: var(--magenta);
  }
  .tag--front .brand-dot {
    width: 120px;
    height: 120px;
    left: 117px;
    top: 230px;
  }
  .tag--front .brand {
    top: 390px;
    font-size: 54px;
  }
  .tagline {
    position: absolute;
    left: 0;
    right: 0;
    top: 520px;
    text-align: center;
    font-family: "Mrs Saint Delafield", cursive;
    font-size: 44px;
    color: var(--ink);
    margin: 0;
    line-height: 1;
  }

  .tag--back .brand {
    top: 248px;
    font-size: 46px;
  }
  .back-band {
    position: absolute;
    inset: auto 0 0 0;
    height: 160px;
    background: linear-gradient(to bottom, var(--card) 0%, var(--magenta-soft) 45%, var(--magenta-deep) 100%);
  }
  .gymnasts-photo {
    position: absolute;
    left: 4px;
    top: 312px;
    width: 346px;
    height: 277px;
    border-radius: 6px 6px 0 0;
    background: linear-gradient(160deg, rgba(217,169,138,0.55) 0%, rgba(34,34,38,0.75) 55%, rgba(208,23,127,0.6) 100%);
  }
</style>
</head>
<body>
<main class="canvas">
  <section class="tag tag--front" aria-label="Front of tag">
    <div class="front-band"></div>
    <span class="hole"></span>
    <span class="brand-dot"></span>
    <h1 class="brand">Velora</h1>
    <p class="tagline">Feel the rhythm</p>
  </section>

  <section class="tag tag--back" aria-label="Back of tag">
    <span class="hole"></span>
    <div class="back-band"></div>
    <div class="gymnasts-photo" role="img" aria-label="Photo of two young rhythmic gymnasts in black outfits, seated in a back bend with arms raised"></div>
    <p class="brand">Velora</p>
  </section>
</main>
</body>
</html>
```